On going F&B business needs a new stationery design for festive occasion

Would like something like the attached file, but with a new look. The basis colours should still be green and yellow.

```html
<!DOCTYPE html>
<html lang="en">
<head>
<meta charset="utf-8">
<title>Seri Hijau Eating House – Festive Stationery</title>
<link href="https://fonts.googleapis.com/css2?family=Cabin+Condensed:wght@700&family=Great+Vibes&family=Italianno&family=Proza+Libre&display=swap" rel="stylesheet">
<style>
  :root{
    --bg:#5e5e5e;
    --paper:#f2f2f1;
    --lime:#c6df64;
    --lime-soft:#b9d65e;
    --green:#5fae6a;
    --green-mid:#4f9f55;
    --green-deep:#1f7a35;
    --green-ink:#2a5a36;
    --script:#8cc63f;
    --text:#2b2b2b;
    --faint:#e2e2e1;
    --white:#ffffff;
  }
  *{box-sizing:border-box;margin:0;padding:0}
  html,body{width:1200px;height:674px;overflow:hidden;background:var(--bg)}
  .canvas{position:relative;width:1200px;height:674px}

  /* Letterhead */
  .letterhead{position:absolute;left:73px;top:51px;width:389px;height:550px;background:var(--paper);overflow:hidden}
  .letterhead__band{position:absolute;left:0;top:0;width:14px;height:100%;background:linear-gradient(180deg,var(--lime) 0%,var(--green-mid) 55%,var(--green-deep) 100%)}
  .letterhead__notch{position:absolute;left:14px;top:46px;width:17px;height:32px;background:var(--lime-soft);clip-path:polygon(0 0,100% 50%,0 100%)}
  .letterhead__greeting{position:absolute;left:40px;top:14px;font-family:"Great Vibes",cursive;font-size:20px;color:var(--script);white-space:nowrap}
  .letterhead__mark{position:absolute;left:41px;top:42px;width:38px;height:38px;border-radius:50%;background:var(--green-ink)}
  .letterhead__name{position:absolute;right:194px;top:45px;font-family:"Cabin Condensed",sans-serif;font-weight:700;color:var(--green-ink);line-height:1.05;text-align:right;white-space:nowrap}
  .letterhead__name .line1{display:block;font-size:24px;letter-spacing:.5px}
  .letterhead__name .line2{display:block;font-size:15px;letter-spacing:.5px}
  .letterhead__lanterns{position:absolute;left:296px;top:0;width:88px;height:152px;border-radius:0 0 30px 30px;background:linear-gradient(180deg,rgba(140,198,63,.15) 0%,rgba(140,198,63,.45) 60%,rgba(95,174,106,.7) 100%)}
  .letterhead__mosque{position:absolute;left:16px;top:170px;width:373px;height:390px;border-radius:180px 180px 0 0;background:linear-gradient(180deg,rgba(0,0,0,.02) 0%,rgba(0,0,0,.05) 50%,rgba(0,0,0,.07) 100%)}
  .letterhead__watermark{position:absolute;left:0;width:100%;text-align:center;font-family:"Italianno",cursive;font-size:40px;color:var(--faint);letter-spacing:1px;word-spacing:12px;white-space:nowrap}
  .letterhead__watermark--top{top:178px}
  .letterhead__watermark--bottom{top:227px}
  .contact{position:absolute;left:23px;top:477px;list-style:none;font-family:"Proza Libre",sans-serif;font-size:8.5px;color:var(--text)}
  .contact li{display:flex;align-items:center;height:16.8px;white-space:nowrap}
  .contact svg{width:11px;height:11px;margin-right:7px;flex:none}

  /* Envelope */
  .envelope{position:absolute;left:525px;top:92px;width:422px;height:300px;overflow:hidden;background:var(--lime)}
  .envelope svg{position:absolute;inset:0}
  .envelope__greeting{position:absolute;left:0;width:100%;text-align:center;font-family:"Italianno",cursive;color:var(--white);font-size:38px;letter-spacing:1px;word-spacing:14px;white-space:nowrap}
  .envelope__greeting--top{top:54px;padding-left:8px}
  .envelope__greeting--bottom{top:104px}

  /* Greeting card */
  .card{position:absolute;left:731px;top:296px;width:429px;height:304px;background:linear-gradient(180deg,var(--lime) 0%,#a9d05c 40%,var(--green-mid) 100%);overflow:hidden}
  .card__lanterns{position:absolute;left:20px;top:0;width:395px;height:160px;background:linear-gradient(180deg,rgba(95,174,106,0) 0%,rgba(95,174,106,.22) 100%)}
  .card__mark{position:absolute;left:49px;top:105px;width:86px;height:86px;border-radius:50%;background:var(--white)}
  .card__name{position:absolute;right:48px;top:120px;font-family:"Cabin Condensed",sans-serif;font-weight:700;color:var(--white);line-height:1;text-align:right;white-space:nowrap}
  .card__name .line1{display:block;font-size:46px;letter-spacing:1px}
  .card__name .line2{display:block;font-size:30px;letter-spacing:1px;margin-top:6px}
</style>
</head>
<body>
<main class="canvas">

  <section class="letterhead">
    <div class="letterhead__band"></div>
    <div class="letterhead__notch"></div>
    <div class="letterhead__mosque" role="img" aria-label="Faint mosque silhouette with minarets and domes"></div>
    <div class="letterhead__lanterns" role="img" aria-label="Hanging festive lanterns and small stars"></div>
    <p class="letterhead__greeting">With Best Compliments</p>
    <div class="letterhead__mark"></div>
    <p class="letterhead__name"><span class="line1">SERI HIJAU</span><span class="line2">EATING HOUSE</span></p>
    <p class="letterhead__watermark letterhead__watermark--top">SELAMAT</p>
    <p class="letterhead__watermark letterhead__watermark--bottom">HARI RAYA</p>
    <ul class="contact">
      <li><svg viewBox="0 0 12 12"><circle cx="6" cy="6" r="6" fill="#5fae6a"/><path d="M6 2.5a2.2 2.2 0 0 0-2.2 2.2C3.8 6.4 6 9.5 6 9.5s2.2-3.1 2.2-4.8A2.2 2.2 0 0 0 6 2.5z" fill="#fff"/><circle cx="6" cy="4.7" r=".8" fill="#5fae6a"/></svg>12, Cedar Industrial Park Road 5 #02-08 Singapore 700123</li>
      <li><svg viewBox="0 0 12 12"><circle cx="6" cy="6" r="6" fill="#5fae6a"/><path d="M3.6 3c.5-.4 1-.3 1.2.1l.6 1.1c.2.4 0 .7-.3.9l-.3.2c.3.8.9 1.4 1.7 1.8l.2-.3c.2-.3.6-.4.9-.2l1.1.6c.4.2.5.7.1 1.2-.5.6-1.4.8-2.4.2C4.7 8 3.6 6.6 3.2 5.2c-.2-.9 0-1.7.4-2.2z" fill="#fff"/></svg>6100 2345</li>
      <li><svg viewBox="0 0 12 12"><circle cx="6" cy="6" r="6" fill="#5fae6a"/><rect x="3" y="3.5" width="2" height="5" fill="#fff"/><rect x="5.5" y="3.5" width="3.5" height="5" fill="#fff"/><rect x="6.2" y="4.2" width="2.1" height="1.2" fill="#5fae6a"/></svg>6100 2345</li>
      <li><svg viewBox="0 0 12 12"><circle cx="6" cy="6" r="6" fill="#5fae6a"/><rect x="3" y="4" width="6" height="4.2" fill="#fff"/><path d="M3 4l3 2.3L9 4" fill="none" stroke="#5fae6a" stroke-width=".7"/></svg>hello@serihijau.example</li>
    </ul>
  </section>

  <section class="envelope">
    <svg viewBox="0 0 422 300" width="422" height="300" aria-hidden="true">
      <polygon points="0,300 131,150 200,150 422,300" fill="#5aab68"/>
      <polygon points="0,0 422,0 205,218" fill="#62b070"/>
    </svg>
    <p class="envelope__greeting envelope__greeting--top">SELAMAT</p>
    <p class="envelope__greeting envelope__greeting--bottom">HARI RAYA</p>
  </section>

  <section class="card">
    <div class="card__lanterns" role="img" aria-label="Faint hanging lanterns and stars"></div>
    <div class="card__mark"></div>
    <p class="card__name"><span class="line1">SERI HIJAU</span><span class="line2">EATING HOUSE</span></p>
  </section>

</main>
</body>
</html>
```